I want to upgrade my old template for the registry. I will describe the things I love about it and the things I don't. We will keep the likes and improve the dislikes. I used the Database page as an Example. The colors are important because they will also be the colors for the pages in the database for each horse registered. I listed all the buttons I will need below.

I want to remind creators that I will have a number of pages on the website but only need one template design that will be for all of them. I want a well designed header with the logo, Continental Merivane Pony Society, and the buttons or pages listed on or under the header. I want the header to stand out from the body of the template. The body of the template will be light in color. White, off white, or light tan with texture. I want examples of fonts that might match the style. The footer will be similar to the header. Just doesn't need to be a fancy. I will need coding for this project, too. Feel free to ask questions. I will try to stay active with comments on work submitted. Thanks Everyone.

I was hoping for a design that would be more creative than what I already have. There are a lot of nice designs, but I don't think any of them did anything as far as the header with the same depth and design of the old one. I would like to use elements of the old design Header and have that improved. There were many neat designs and textures for the body but not the header.

Target Market(s)

This is a webpage for a horse Registry. This will appear to horse lovers.

Industry/Entity Type

this is a horse breed registry. We record the heritage of all horses keeping DNA on all animals that qualify to the rules set by the CMPS.

Coding

Coded - Design and coding required

Number of Pages Required

1 page

Colors

Designer to choose colors to be used in the design.

Requirements
Must have
• The same flag/logo design with the shadow behind it as on the old design. A similar header backdrop with damask and texture similar in colors and texture. I think the old one is too gritty. I think the layer is too harsh for the damask. But I like the colors in the grunge layer over the damask. Flag/logo on the left side similar to the old design. The header must be about the same size. It needs a new content body. I love vintage but not old yellow orange or pink paper. Something light with texture like some of white and off white I have seen in the designs. The footer will have similar design as the header. Doesn't need to be as elaborate, but related. Buttons will be: Home, The Merivane, Registration, News & Events, Store, Database. There is no need to do a page for each. Just one stunning template design that I will use for each page.
Nice to have
• I like an elegant design with a mix of matching colors (browns, tans, cremes, whites), patterns (damask, pin stripes), and textures (paper texture. Soft and small not hard or large textures like wrinkles). I am open to fonts. Maybe a little more modern type. Surprise me.
Should not have
• I do not want a photos, graphics, or phrases attached to or in the header. I want the header to stand alone. I don't want a western American cowboy feel to the template. I don't want a lot of dark colors in the body where content will go.

```html
<!DOCTYPE html>
<html lang="en">
<head>
<meta charset="utf-8">
<title>Continental Merivane Pony Society – Page Template</title>
<link href="https://fonts.googleapis.com/css2?family=Cinzel:wght@400;700&family=Lato:ital,wght@0,400;0,700;1,400&display=swap" rel="stylesheet">
<style>
:root{
  --board:#8a8a8a;
  --brown-deep:#2e1a10;
  --brown-dark:#3e2416;
  --brown:#5a3722;
  --brown-mid:#7a5236;
  --brown-soft:#9a714f;
  --tan:#e6d3ad;
  --tan-light:#f3e8d2;
  --cream:#f8f1e2;
  --paper:#f3f2ef;
  --gray-light:#e2e1dc;
  --ink:#4a2f1e;
  --muted:#8a7a68;
  --gold:#c9a66b;
  --gold-light:#e2c893;
  --photo-a:#c2ad90;
  --photo-b:#86705a;
}
*{box-sizing:border-box;margin:0;padding:0}
html,body{width:885px;height:1200px;overflow:hidden}
body{background:var(--board);font-family:'Lato',sans-serif;color:var(--ink);position:relative}
.board{position:absolute;top:22px;left:40px;right:40px;display:flex;justify-content:space-between}
.page{width:240px;height:1150px;display:flex;flex-direction:column;box-shadow:0 3px 8px rgba(0,0,0,.4);overflow:hidden;background:var(--cream)}

/* shared */
.photo{background:linear-gradient(160deg,var(--photo-a),var(--photo-b));border:2px solid #fff;box-shadow:0 1px 3px rgba(0,0,0,.3)}
.heading{font-family:'Cinzel',serif;font-weight:700;font-size:11px;letter-spacing:1px;color:var(--ink);text-align:center;display:flex;align-items:center;justify-content:center;gap:6px}
.heading.ruled::before,.heading.ruled::after{content:"";width:22px;height:1px;background:var(--brown-soft)}
.subline{font-size:6px;font-style:italic;color:var(--muted);text-align:center;margin-top:2px}
.copy{font-size:6px;line-height:1.45;color:var(--muted)}
.button{display:inline-block;background:var(--brown);color:var(--cream);font-size:6px;font-weight:700;padding:3px 9px;letter-spacing:.6px;text-transform:uppercase;border:1px solid var(--brown-dark)}
.frame{border:1px solid var(--brown-mid);border-radius:6px;padding:6px 18px;outline:1px solid var(--brown-mid);outline-offset:2px;background:var(--cream)}

/* header */
.site-header{height:170px;position:relative;overflow:hidden;
  background:
    repeating-linear-gradient(90deg,rgba(255,235,200,.05) 0 1px,transparent 1px 6px),
    radial-gradient(ellipse at 50% 45%,var(--brown-soft) 0%,var(--brown-mid) 30%,var(--brown-dark) 70%,var(--brown-deep) 100%);}
.damask-texture{position:absolute;inset:14px 0 24px 0;opacity:.35;
  background:
    radial-gradient(circle at 20% 30%,rgba(226,200,147,.5),transparent 18%),
    radial-gradient(circle at 50% 65%,rgba(226,200,147,.45),transparent 20%),
    radial-gradient(circle at 80% 30%,rgba(226,200,147,.5),transparent 18%),
    radial-gradient(circle at 35% 85%,rgba(226,200,147,.3),transparent 15%),
    radial-gradient(circle at 65% 10%,rgba(226,200,147,.3),transparent 15%);}
.grunge-layer{position:absolute;inset:0;background:radial-gradient(ellipse at 50% 50%,transparent 40%,rgba(20,10,5,.55) 100%)}
.topbar{position:relative;height:14px;background:rgba(0,0,0,.4);border-bottom:1px solid rgba(201,166,107,.4);display:flex;justify-content:space-between;align-items:center;padding:0 8px;font-size:5.5px;color:var(--gold-light);letter-spacing:.4px}
.brand{position:absolute;top:38px;left:14px;display:flex;align-items:center;gap:7px}
.brand-mark{width:34px;height:34px;border-radius:50%;background:var(--cream);flex:none;box-shadow:0 2px 5px rgba(0,0,0,.5)}
.brand-plate{background:linear-gradient(var(--cream),var(--tan));padding:6px 9px;box-shadow:3px 4px 8px rgba(0,0,0,.55);border:1px solid var(--gold)}
.brand-name{font-family:'Cinzel',serif;font-size:8px;font-weight:700;color:var(--brown-dark);line-height:1.3;letter-spacing:.3px}
.page--centered .brand{left:50%;transform:translateX(-50%);flex-direction:column;top:22px;text-align:center;gap:6px}
.page--centered .brand-mark{width:46px;height:46px}
.header-rule{position:absolute;left:14px;right:14px;bottom:30px;height:3px;border-top:1px solid var(--gold);border-bottom:1px solid var(--gold);opacity:.6}
.main-nav{position:absolute;bottom:0;left:0;right:0;height:22px;background:linear-gradient(var(--brown-deep),#1f120a);border-top:1px solid var(--gold);display:flex;justify-content:space-around;align-items:center;padding:0 3px}
.main-nav a{font-size:5.5px;font-weight:700;color:var(--gold-light);text-decoration:none;letter-spacing:.3px;text-transform:uppercase}
.main-nav a.current{color:#fff}

/* breed */
.section-breed{height:150px;padding:12px 10px;
  background:repeating-linear-gradient(90deg,rgba(150,110,60,.05) 0 1px,transparent 1px 5px),linear-gradient(var(--tan-light),var(--tan))}
.breed-row{display:flex;justify-content:space-between;margin-top:10px}
.breed-card{width:50px;text-align:center}
.breed-card .photo{width:50px;height:40px}
.breed-card span{display:block;font-size:5.5px;color:var(--ink);margin-top:3px;font-weight:700}
.section-breed .copy{text-align:center;margin-top:8px}
.dots{display:flex;justify-content:center;gap:4px;margin-top:7px}
.dots i{width:4px;height:4px;border-radius:50%;background:var(--brown-soft)}
.dots i:first-child{background:var(--brown)}

/* registration */
.section-registration{height:112px;background:var(--paper);display:flex;flex-direction:column;align-items:center;justify-content:center;gap:7px;padding:0 24px;text-align:center}

/* news */
.section-news{height:165px;padding:12px 10px;background:repeating-linear-gradient(90deg,rgba(150,110,60,.04) 0 1px,transparent 1px 5px),var(--cream)}
.news-grid{display:flex;gap:8px;margin-top:9px}
.news-feature{width:100px}
.news-feature .photo{width:100px;height:72px}
.news-feature p{font-size:6px;font-weight:700;margin-top:4px}
.news-feature .copy{font-weight:400;margin-top:1px}
.news-list{flex:1;display:flex;flex-direction:column;gap:6px}
.news-item{display:flex;gap:4px;align-items:center}
.news-item .photo{width:26px;height:20px;flex:none;border-width:1px}
.news-item div:last-child{font-size:6px;line-height:1.3;font-weight:700}
.news-item small{display:block;font-size:5px;font-weight:400;color:var(--muted)}
.news-list .button{align-self:flex-start;margin-top:2px}

/* store */
.section-store{height:160px;background:linear-gradient(var(--paper),var(--gray-light));display:flex;flex-direction:column;align-items:center;padding-top:14px;gap:10px}
.products{display:flex;gap:12px;align-items:flex-start}
.product{text-align:center;width:40px}
.product span{display:block;width:36px;height:36px;margin:0 auto;border-radius:50%;background:radial-gradient(circle at 40% 35%,#e2d3bb,#6b4a32);box-shadow:0 2px 3px rgba(0,0,0,.25)}
.product p{font-size:5.5px;margin-top:4px;font-weight:700}
.product small{font-size:5.5px;color:var(--brown-mid)}
.store-more{display:flex;align-items:center;gap:4px;font-size:6px;color:var(--brown);font-weight:700}

/* database */
.section-database{height:160px;padding:13px 12px;background:repeating-linear-gradient(90deg,rgba(150,110,60,.05) 0 1px,transparent 1px 5px),linear-gradient(var(--tan-light),var(--tan))}
.section-database .heading{justify-content:flex-start}
.db-body{display:flex;gap:8px;margin-top:8px}
.db-photos{display:flex;gap:5px}
.db-card .photo{width:46px;height:40px}
.db-card span{display:block;font-size:5.5px;font-weight:700;margin-top:3px;text-align:center}
.db-side{flex:1;display:flex;flex-direction:column;gap:6px}
.search{display:flex;gap:3px}
.field{height:13px;background:#fff;border:1px solid #d8cdb8;font-size:5.5px;color:var(--muted);padding:3px 4px;flex:1}

/* contact */
.section-contact{height:143px;background:var(--cream);padding:13px 12px;display:flex;gap:10px}
.contact-form{flex:1;display:flex;flex-direction:column;gap:4px}
.contact-form .heading{justify-content:flex-start;margin-bottom:2px}
.field.tall{height:26px;flex:none}
.contact-form .field{flex:none}
.contact-form .button{align-self:flex-start}
.contact-photo{width:74px;height:110px;border:none;box-shadow:none;background:linear-gradient(180deg,var(--cream),#c7b190 60%,#a89072)}

/* footer */
.site-footer{height:90px;position:relative;padding:12px 12px;display:flex;gap:10px;color:var(--tan);
  background:repeating-linear-gradient(90deg,rgba(255,235,200,.05) 0 1px,transparent 1px 6px),radial-gradient(ellipse at 40% 40%,var(--brown-mid),var(--brown-dark) 70%,var(--brown-deep));border-top:2px solid var(--gold)}
.footer-brand{display:flex;flex-direction:column;align-items:center;gap:4px;width:58px;text-align:center}
.footer-brand .brand-mark{width:28px;height:28px}
.footer-brand .brand-name{font-size:5.5px;color:var(--gold-light)}
.footer-links{display:flex;flex-direction:column;gap:4px;font-size:5.5px;flex:1}
.footer-links b{font-family:'Cinzel',serif;font-size:6.5px;color:var(--gold-light)}
.footer-art{width:56px;height:60px;align-self:flex-end;background:linear-gradient(var(--brown-mid),var(--brown-dark));opacity:.7}
</style>
</head>
<body>
<div class="board">

<div class="page">
  <header class="site-header">
    <div class="damask-texture" role="img" aria-label="Soft damask pattern"></div>
    <div class="grunge-layer"></div>
    <div class="topbar"><span>Welcome to the Society</span><span>Log in · Members</span></div>
    <div class="brand"><div class="brand-mark"></div><div class="brand-plate"><div class="brand-name">Continental<br>Merivane Pony<br>Society</div></div></div>
    <div class="header-rule"></div>
    <nav class="main-nav"><a class="current">Home</a><a>The Merivane</a><a>Registration</a><a>News &amp; Events</a><a>Store</a><a>Database</a></nav>
  </header>
  <section class="section-breed">
    <h2 class="heading ruled">The Merivane</h2>
    <p class="subline">Preserving every bloodline since our founding</p>
    <div class="breed-row">
      <div class="breed-card"><div class="photo" role="img" aria-label="Merivane mare photo"></div><span>Mares</span></div>
      <div class="breed-card"><div class="photo" role="img" aria-label="Merivane stallion photo"></div><span>Stallions</span></div>
      <div class="breed-card"><div class="photo" role="img" aria-label="Merivane foal photo"></div><span>Foals</span></div>
      <div class="breed-card"><div class="photo" role="img" aria-label="Merivane gelding photo"></div><span>Geldings</span></div>
    </div>
    <p class="copy">A gentle spotted breed prized for stamina and calm temper.</p>
    <div class="dots"><i></i><i></i><i></i></div>
  </section>
  <section class="section-registration">
    <div class="frame"><h2 class="heading">Registration</h2></div>
    <p class="copy">Record your pony's pedigree, DNA and markings with the society.</p>
    <span class="button">Register now</span>
  </section>
  <section class="section-news">
    <h2 class="heading ruled">News &amp; Events</h2>
    <p class="subline">Latest from the society</p>
    <div class="news-grid">
      <div class="news-feature"><div class="photo" role="img" aria-label="Featured event photo of ponies"></div><p>Summer Breed Show<span class="copy" style="display:block">Entries open until July</span></p></div>
      <div class="news-list">
        <div class="news-item"><div class="photo" role="img" aria-label="News thumbnail"></div><div>Spring show results<small>April 12</small></div></div>
        <div class="news-item"><div class="photo" role="img" aria-label="News thumbnail"></div><div>Foal of the year<small>May 03</small></div></div>
        <div class="news-item"><div class="photo" role="img" aria-label="News thumbnail"></div><div>Breeders meeting<small>June 20</small></div></div>
        <span class="button">View all</span>
      </div>
    </div>
  </section>
  <section class="section-store">
    <div class="frame"><h2 class="heading">Store</h2></div>
    <div class="products">
      <div class="product"><span role="img" aria-label="Store product"></span><p>Halter</p><small>$24</small></div>
      <div class="product"><span role="img" aria-label="Store product"></span><p>Cap</p><small>$18</small></div>
      <div class="product"><span role="img" aria-label="Store product"></span><p>Mug</p><small>$12</small></div>
      <div class="product"><span role="img" aria-label="Store product"></span><p>Blanket</p><small>$40</small></div>
    </div>
    <div class="store-more">Shop all <svg width="8" height="8" viewBox="0 0 8 8"><path d="M1 4h6M4 1l3 3-3 3" stroke="#5a3722" fill="none" stroke-width="1.2"/></svg></div>
  </section>
  <section class="section-database">
    <h2 class="heading">Database</h2>
    <p class="subline" style="text-align:left">Every registered pony in one place</p>
    <div class="db-body">
      <div class="db-photos">
        <div class="db-card"><div class="photo" role="img" aria-label="Registered pony photo"></div><span>Silver Fern</span></div>
        <div class="db-card"><div class="photo" role="img" aria-label="Registered pony photo"></div><span>Oak Dancer</span></div>
      </div>
      <div class="db-side">
        <p class="copy">Search by name, number or bloodline.</p>
        <div class="search"><div class="field">Pony name</div></div>
        <span class="button" style="align-self:flex-start">Search</span>
      </div>
    </div>
  </section>
  <section class="section-contact">
    <div class="contact-form">
      <h2 class="heading">Get in Touch</h2>
      <div class="field">Name</div><div class="field">Email</div><div class="field tall">Message</div>
      <span class="button">Send</span>
    </div>
    <div class="photo contact-photo" role="img" aria-label="Portrait of a grey pony"></div>
  </section>
  <footer class="site-footer">
    <div class="footer-brand"><div class="brand-mark"></div><div class="brand-name">Continental Merivane Pony Society</div></div>
    <div class="footer-links"><b>Contact</b><span>office@merivane-society.org</span><span>Privacy · Terms</span><span>© CMPS. All rights reserved</span></div>
    <div class="footer-art" role="img" aria-label="Galloping pony decoration"></div>
  </footer>
</div>

<div class="page page--centered">
  <header class="site-header">
    <div class="damask-texture" role="img" aria-label="Soft damask pattern"></div>
    <div class="grunge-layer"></div>
    <div class="topbar"><span>Welcome to the Society</span><span>Log in · Members</span></div>
    <div class="brand"><div class="brand-mark"></div><div class="brand-plate"><div class="brand-name">Continental Merivane<br>Pony Society</div></div></div>
    <div class="header-rule"></div>
    <nav class="main-nav"><a class="current">Home</a><a>The Merivane</a><a>Registration</a><a>News &amp; Events</a><a>Store</a><a>Database</a></nav>
  </header>
  <section class="section-breed">
    <h2 class="heading ruled">The Merivane</h2>
    <p class="subline">Preserving every bloodline since our founding</p>
    <div class="breed-row">
      <div class="breed-card"><div class="photo" role="img" aria-label="Merivane mare photo"></div><span>Mares</span></div>
      <div class="breed-card"><div class="photo" role="img" aria-label="Merivane stallion photo"></div><span>Stallions</span></div>
      <div class="breed-card"><div class="photo" role="img" aria-label="Merivane foal photo"></div><span>Foals</span></div>
      <div class="breed-card"><div class="photo" role="img" aria-label="Merivane gelding photo"></div><span>Geldings</span></div>
    </div>
    <p class="copy">A gentle spotted breed prized for stamina and calm temper.</p>
    <div class="dots"><i></i><i></i><i></i></div>
  </section>
  <section class="section-registration">
    <div class="frame"><h2 class="heading">Registration</h2></div>
    <p class="copy">Record your pony's pedigree, DNA and markings with the society.</p>
    <span class="button">Register now</span>
  </section>
  <section class="section-news">
    <h2 class="heading ruled">News &amp; Events</h2>
    <p class="subline">Latest from the society</p>
    <div class="news-grid">
      <div class="news-feature"><div class="photo" role="img" aria-label="Featured event photo of ponies"></div><p>Summer Breed Show<span class="copy" style="display:block">Entries open until July</span></p></div>
      <div class="news-list">
        <div class="news-item"><div class="photo" role="img" aria-label="News thumbnail"></div><div>Spring show results<small>April 12</small></div></div>
        <div class="news-item"><div class="photo" role="img" aria-label="News thumbnail"></div><div>Foal of the year<small>May 03</small></div></div>
        <div class="news-item"><div class="photo" role="img" aria-label="News thumbnail"></div><div>Breeders meeting<small>June 20</small></div></div>
        <span class="button">View all</span>
      </div>
    </div>
  </section>
  <section class="section-store">
    <div class="frame"><h2 class="heading">Store</h2></div>
    <div class="products">
      <div class="product"><span role="img" aria-label="Store product"></span><p>Halter</p><small>$24</small></div>
      <div class="product"><span role="img" aria-label="Store product"></span><p>Cap</p><small>$18</small></div>
      <div class="product"><span role="img" aria-label="Store product"></span><p>Mug</p><small>$12</small></div>
      <div class="product"><span role="img" aria-label="Store product"></span><p>Blanket</p><small>$40</small></div>
    </div>
    <div class="store-more">Shop all <svg width="8" height="8" viewBox="0 0 8 8"><path d="M1 4h6M4 1l3 3-3 3" stroke="#5a3722" fill="none" stroke-width="1.2"/></svg></div>
  </section>
  <section class="section-database">
    <h2 class="heading">Database</h2>
    <p class="subline" style="text-align:left">Every registered pony in one place</p>
    <div class="db-body">
      <div class="db-photos">
        <div class="db-card"><div class="photo" role="img" aria-label="Registered pony photo"></div><span>Silver Fern</span></div>
        <div class="db-card"><div class="photo" role="img" aria-label="Registered pony photo"></div><span>Oak Dancer</span></div>
      </div>
      <div class="db-side">
        <p class="copy">Search by name, number or bloodline.</p>
        <div class="search"><div class="field">Pony name</div></div>
        <span class="button" style="align-self:flex-start">Search</span>
      </div>
    </div>
  </section>
  <section class="section-contact">
    <div class="contact-form">
      <h2 class="heading">Get in Touch</h2>
      <div class="field">Name</div><div class="field">Email</div><div class="field tall">Message</div>
      <span class="button">Send</span>
    </div>
    <div class="photo contact-photo" role="img" aria-label="Portrait of a grey pony"></div>
  </section>
  <footer class="site-footer">
    <div class="footer-brand"><div class="brand-mark"></div><div class="brand-name">Continental Merivane Pony Society</div></div>
    <div class="footer-links"><b>Contact</b><span>office@merivane-society.org</span><span>Privacy · Terms</span><span>© CMPS. All rights reserved</span></div>
    <div class="footer-art" role="img" aria-label="Galloping pony decoration"></div>
  </footer>
</div>

<div class="page">
  <header class="site-header">
    <div class="damask-texture" role="img" aria-label="Soft damask pattern"></div>
    <div class="grunge-layer"></div>
    <div class="topbar"><span>Welcome to the Society</span><span>Log in · Members</span></div>
    <div class="brand"><div class="brand-mark"></div><div class="brand-plate"><div class="brand-name">Continental<br>Merivane Pony<br>Society</div></div></div>
    <div class="header-rule"></div>
    <nav class="main-nav"><a class="current">Home</a><a>The Merivane</a><a>Registration</a><a>News &amp; Events</a><a>Store</a><a>Database</a></nav>
  </header>
  <section class="section-breed">
    <h2 class="heading ruled">The Merivane</h2>
    <p class="subline">Preserving every bloodline since our founding</p>
    <div class="breed-row">
      <div class="breed-card"><div class="photo" role="img" aria-label="Merivane mare photo"></div><span>Mares</span></div>
      <div class="breed-card"><div class="photo" role="img" aria-label="Merivane stallion photo"></div><span>Stallions</span></div>
      <div class="breed-card"><div class="photo" role="img" aria-label="Merivane foal photo"></div><span>Foals</span></div>
      <div class="breed-card"><div class="photo" role="img" aria-label="Merivane gelding photo"></div><span>Geldings</span></div>
    </div>
    <p class="copy">A gentle spotted breed prized for stamina and calm temper.</p>
    <div class="dots"><i></i><i></i><i></i></div>
  </section>
  <section class="section-registration">
    <div class="frame"><h2 class="heading">Registration</h2></div>
    <p class="copy">Record your pony's pedigree, DNA and markings with the society.</p>
    <span class="button">Register now</span>
  </section>
  <section class="section-news">
    <h2 class="heading ruled">News &amp; Events</h2>
    <p class="subline">Latest from the society</p>
    <div class="news-grid">
      <div class="news-feature"><div class="photo" role="img" aria-label="Featured event photo of ponies"></div><p>Summer Breed Show<span class="copy" style="display:block">Entries open until July</span></p></div>
      <div class="news-list">
        <div class="news-item"><div class="photo" role="img" aria-label="News thumbnail"></div><div>Spring show results<small>April 12</small></div></div>
        <div class="news-item"><div class="photo" role="img" aria-label="News thumbnail"></div><div>Foal of the year<small>May 03</small></div></div>
        <div class="news-item"><div class="photo" role="img" aria-label="News thumbnail"></div><div>Breeders meeting<small>June 20</small></div></div>
        <span class="button">View all</span>
      </div>
    </div>
  </section>
  <section class="section-store">
    <div class="frame"><h2 class="heading">Store</h2></div>
    <div class="products">
      <div class="product"><span role="img" aria-label="Store product"></span><p>Halter</p><small>$24</small></div>
      <div class="product"><span role="img" aria-label="Store product"></span><p>Cap</p><small>$18</small></div>
      <div class="product"><span role="img" aria-label="Store product"></span><p>Mug</p><small>$12</small></div>
      <div class="product"><span role="img" aria-label="Store product"></span><p>Blanket</p><small>$40</small></div>
    </div>
    <div class="store-more">Shop all <svg width="8" height="8" viewBox="0 0 8 8"><path d="M1 4h6M4 1l3 3-3 3" stroke="#5a3722" fill="none" stroke-width="1.2"/></svg></div>
  </section>
  <section class="section-database">
    <h2 class="heading">Database</h2>
    <p class="subline" style="text-align:left">Every registered pony in one place</p>
    <div class="db-body">
      <div class="db-photos">
        <div class="db-card"><div class="photo" role="img" aria-label="Registered pony photo"></div><span>Silver Fern</span></div>
        <div class="db-card"><div class="photo" role="img" aria-label="Registered pony photo"></div><span>Oak Dancer</span></div>
      </div>
      <div class="db-side">
        <p class="copy">Search by name, number or bloodline.</p>
        <div class="search"><div class="field">Pony name</div></div>
        <span class="button" style="align-self:flex-start">Search</span>
      </div>
    </div>
  </section>
  <section class="section-contact">
    <div class="contact-form">
      <h2 class="heading">Get in Touch</h2>
      <div class="field">Name</div><div class="field">Email</div><div class="field tall">Message</div>
      <span class="button">Send</span>
    </div>
    <div class="photo contact-photo" role="img" aria-label="Portrait of a grey pony"></div>
  </section>
  <footer class="site-footer">
    <div class="footer-brand"><div class="brand-mark"></div><div class="brand-name">Continental Merivane Pony Society</div></div>
    <div class="footer-links"><b>Contact</b><span>office@merivane-society.org</span><span>Privacy · Terms</span><span>© CMPS. All rights reserved</span></div>
    <div class="footer-art" role="img" aria-label="Galloping pony decoration"></div>
  </footer>
</div>

</div>
</body>
</html>
```